Animal Eye Clinic needs a Business card

We are a new veterinary ophthalmology practice (Tessaly Animal Eye Care) and we need a business card designed. We only see animal eyes - we are not a regular veterinary clinic. We already have a logo. We are looking for a professional, good looking business card to hand out to our clients. We are looking for something simple but professional and contemporary. Our logo is likely the only picture/graphic that needs to be on the card.
Updates

Contact Information for Business Card

Marisol Dunkley, BSc, DVM, MSc, DipACVO
Veterinary Ophthalmologist

Phone: 250.418.3097
Email: tessalyanimaleyecare@mailbrook.net
Website: tessalyanimaleyecare.net
Address: 1840 Pellworth Rd
Kelowna, BC, V4T 8M3

Colors

Designer to choose colors to be used in the design.

Requirements
Must have
• Our logo (attached)

```html
<!DOCTYPE html>
<html lang="en">
<head>
<meta charset="utf-8">
<title>Tessaly Animal Eye Care – Business Card</title>
<link rel="stylesheet" href="https://fonts.googleapis.com/css2?family=Montserrat:wght@600;700&family=Open+Sans:wght@400;600&display=swap">
<style>
  :root {
    --backdrop: #006fae;
    --teal: #0097a7;
    --grey: #6d6e70;
    --white: #ffffff;
    --icon-bg: #f1f1f1;
  }
  * { margin: 0; padding: 0; box-sizing: border-box; }
  html, body { width: 1200px; height: 1200px; overflow: hidden; }
  body { background: var(--backdrop); position: relative; font-family: "Open Sans", sans-serif; }

  .card { position: absolute; left: 192px; width: 816px; background: var(--white); overflow: hidden; }
  .card--front { top: 114px; height: 477px; }
  .card--back { top: 614px; height: 470px; }

  .brand { position: absolute; display: flex; align-items: center; color: var(--teal); font-family: "Montserrat", sans-serif; font-weight: 700; }
  .brand__mark { border-radius: 50%; background: var(--teal); flex: none; }
  .brand__name { display: flex; flex-direction: column; line-height: 1; }
  .brand__place { text-transform: uppercase; }
  .brand__line { text-transform: uppercase; white-space: nowrap; }

  .brand--large { left: 46px; top: 116px; }
  .brand--large .brand__mark { width: 168px; height: 168px; margin-right: 44px; }
  .brand--large .brand__place { font-size: 38px; letter-spacing: 0.62em; margin-bottom: 14px; }
  .brand--large .brand__line { font-size: 55px; letter-spacing: -0.01em; }

  .brand--small { left: 456px; top: 54px; }
  .brand--small .brand__mark { width: 80px; height: 80px; margin-right: 18px; }
  .brand--small .brand__place { font-size: 18px; letter-spacing: 0.6em; margin-bottom: 6px; }
  .brand--small .brand__line { font-size: 26px; letter-spacing: -0.01em; }

  .footer-band { position: absolute; left: 0; right: 0; bottom: 0; height: 117px; background: var(--teal); }
  .footer-band__slant { position: absolute; left: 0; bottom: 0; }
  .footer-band__url { position: absolute; left: 54px; color: var(--white); font-weight: 600; font-size: 23px; letter-spacing: 0.01em; }
  .social { position: absolute; display: flex; gap: 14px; }
  .social__dot { width: 50px; height: 50px; border-radius: 50%; background: var(--icon-bg); }

  .card--front .footer-band__url { top: 44px; }
  .card--front .social { right: 43px; top: 34px; }

  .person { position: absolute; left: 44px; top: 46px; font-family: "Montserrat", sans-serif; }
  .person__name { color: var(--teal); font-size: 37px; font-weight: 700; letter-spacing: 0.01em; line-height: 1.1; }
  .person__credentials { color: var(--grey); font-size: 24px; font-weight: 600; line-height: 1.2; margin-top: 2px; }
  .person__title { color: var(--grey); font-size: 19px; font-weight: 600; letter-spacing: 0.02em; margin-top: 2px; }

  .accent-bar { position: absolute; left: 0; top: 155px; width: 14px; height: 167px; background: var(--teal); }

  .contact { position: absolute; left: 42px; top: 188px; list-style: none; }
  .contact__item { display: flex; align-items: center; height: 36.5px; color: var(--grey); font-size: 20.5px; }
  .contact__icon { width: 28px; height: 28px; margin-right: 10px; fill: var(--teal); flex: none; }

  .card--back .footer-band__url { left: 54px; bottom: 32px; }
  .card--back .social { right: 43px; bottom: 14px; }
</style>
</head>
<body>

<section class="card card--front">
  <div class="brand brand--large">
    <span class="brand__mark"></span>
    <span class="brand__name">
      <span class="brand__place">Tessaly</span>
      <span class="brand__line">Animal Eye Care</span>
    </span>
  </div>
  <div class="footer-band">
    <span class="footer-band__url">TESSALYANIMALEYECARE.NET</span>
    <div class="social">
      <span class="social__dot"></span>
      <span class="social__dot"></span>
    </div>
  </div>
</section>

<section class="card card--back">
  <div class="person">
    <h1 class="person__name">MARISOL DUNKLEY</h1>
    <p class="person__credentials">BSC, DVM, MSC, DIPACVO</p>
    <p class="person__title">VETERINARY OPHTHALMOLOGIST</p>
  </div>

  <div class="brand brand--small">
    <span class="brand__mark"></span>
    <span class="brand__name">
      <span class="brand__place">Tessaly</span>
      <span class="brand__line">Animal Eye Care</span>
    </span>
  </div>

  <span class="accent-bar"></span>

  <ul class="contact">
    <li class="contact__item">
      <svg class="contact__icon" viewBox="0 0 24 24"><path d="M6.6 10.8a15 15 0 0 0 6.6 6.6l2.2-2.2c.3-.3.7-.4 1-.2 1.1.4 2.3.6 3.6.6.6 0 1 .4 1 1V20c0 .6-.4 1-1 1A17 17 0 0 1 3 4c0-.6.4-1 1-1h3.5c.6 0 1 .4 1 1 0 1.3.2 2.5.6 3.6.1.3 0 .7-.2 1z"/></svg>
      250.418.3097
    </li>
    <li class="contact__item">
      <svg class="contact__icon" viewBox="0 0 24 24"><path d="M2 5h20v14H2z M4 7v.4l8 5.6 8-5.6V7H4zm0 2.8V17h16V9.8l-8 5.6z" fill-rule="evenodd"/></svg>
      tessalyanimaleyecare@mailbrook.net
    </li>
    <li class="contact__item">
      <svg class="contact__icon" viewBox="0 0 24 24"><circle cx="12" cy="12" r="10"/><path d="M2 12h20M12 2c3 3 3 17 0 20M12 2c-3 3-3 17 0 20M4 7h16M4 17h16" stroke="#fff" stroke-width="1.2" fill="none"/></svg>
      tessalyanimaleyecare.net
    </li>
    <li class="contact__item">
      <svg class="contact__icon" viewBox="0 0 24 24"><path d="M12 3 1 12h3v9h6v-6h4v6h6v-9h3z"/></svg>
      1840 Pellworth Rd Kelowna, BC, V4T 8M3
    </li>
  </ul>

  <svg class="footer-band__slant" width="816" height="128" viewBox="0 0 816 128" aria-hidden="true">
    <polygon points="0,48 816,0 816,128 0,128" fill="var(--teal)"/>
  </svg>
  <span class="footer-band__url">TESSALYANIMALEYECARE.NET</span>
  <div class="social">
    <span class="social__dot"></span>
    <span class="social__dot"></span>
  </div>
</section>

</body>
</html>
```